B.P.L.H. Letterhead design

I would like a really professionally designed letterhead for my professional tutoring business called "The Bright Pathway Learning House" (B.P.L.H.).Something fresh,modern and inspiring that will breath new life into the bu.The business/centre offers professional tutoring for 6 - 16 year olds in maths and english.

I have also attached a centre picture our logo, our proposed school bag,and our latest newsletter to give some perspective & background.

We like to see designs that use the blue & yellow colour theme.The final design should communicate ... "Giving Your Child A Secure Future ... And You Yourself ... Peace Of Mind!!!"

```html
<!DOCTYPE html>
<html lang="en">
<head>
<meta charset="utf-8">
<title>B.P.L.H. Letterhead</title>
<link href="https://fonts.googleapis.com/css2?family=Carlito:wght@400;700&display=swap" rel="stylesheet">
<style>
  :root {
    --page: #ffffff;
    --edge: #8a8a8a;
    --navy: #1f2a63;
    --navy-deep: #18204f;
    --gold: #f2b817;
    --ink: #1a1a1a;
    --mist: #ececec;
  }
  html, body {
    margin: 0;
    padding: 0;
    width: 929px;
    height: 1200px;
    overflow: hidden;
    background: var(--page);
  }
  .letterhead {
    position: relative;
    width: 929px;
    height: 1200px;
    box-sizing: border-box;
    border: 1px solid var(--edge);
    background: var(--page);
    font-family: "Carlito", "Calibri", sans-serif;
    color: var(--ink);
    overflow: hidden;
  }
  .brand-panel {
    position: absolute;
    left: 0;
    top: 29px;
    width: 310px;
    height: 155px;
    background: linear-gradient(135deg, var(--navy) 0%, var(--navy-deep) 100%);
    display: flex;
    align-items: center;
    justify-content: center;
    gap: 12px;
    padding: 0 18px;
    box-sizing: border-box;
  }
  .brand-mark {
    width: 16px;
    height: 16px;
    flex: none;
    background: var(--gold);
  }
  .brand-name {
    margin: 0;
    font-size: 24px;
    font-weight: 400;
    line-height: 1.15;
    color: var(--gold);
  }
  .contact {
    position: absolute;
    right: 22px;
    top: 33px;
    text-align: right;
    font-size: 15.5px;
    line-height: 21.7px;
    font-style: normal;
  }
  .contact .phone {
    margin-top: 19px;
  }
  .backdrop-name {
    position: absolute;
    left: 100px;
    top: 830px;
    width: 745px;
    margin: 0;
    text-align: center;
    font-size: 220px;
    font-weight: 700;
    line-height: 1;
    letter-spacing: 4px;
    color: var(--mist);
    white-space: nowrap;
    user-select: none;
  }
  .backdrop-mark {
    position: absolute;
    left: 432px;
    top: 722px;
    width: 70px;
    height: 70px;
    background: var(--mist);
  }
</style>
</head>
<body>
  <main class="letterhead">
    <header>
      <div class="brand-panel">
        <span class="brand-mark"></span>
        <h1 class="brand-name">The Bright Pathway Learning House</h1>
      </div>
      <address class="contact">
        <div>22 - 26 Maple Row</div>
        <div>Elm Gardens</div>
        <div>Northbrook</div>
        <div>Westford</div>
        <div>WF2 7LB</div>
        <div class="phone">Tel 0207 555 0148</div>
      </address>
    </header>
    <span class="backdrop-mark" aria-hidden="true"></span>
    <p class="backdrop-name" aria-hidden="true">B.P.L.H.</p>
  </main>
</body>
</html>
```